Business Card Design

I need a business card design for my law office based in Pasadena, California. I am a sole practitioner and I specialize in business transaction and litigation, probate and estate planning, taxation law, corporate and business formation, immigration and real estate. I want something that is simple, yet stands out.

A friend helped to create a logo about 6 years ago. I am open to new ideas to changing the logo.

Industry/Entity Type

Business

Contact Information for Business Card

Law Offices of Doran M. Vaske
482 W. Harlow Ave., Suite 312
Pasadena, CA 91108
Tel: 626-503-7719
Fax: 626-581-9046
Email: dvaske@dmvlegalgrp.example

Attorney: Doran M. Vaske

```html
<!DOCTYPE html>
<html lang="en">
<head>
<meta charset="utf-8">
<title>Doran M. Vaske Law Office — Business Cards</title>
<link rel="stylesheet" href="https://fonts.googleapis.com/css2?family=Open+Sans:wght@300;400;700&display=swap">
<style>
  :root {
    --canvas: #e9e7e3;
    --card: #fbfbfb;
    --ink: #2b2b2b;
    --ink-soft: #555555;
    --grey-dark: #3a3a3a;
    --grey-mid: #9a9a9a;
    --grey-light: #d9d9d9;
    --shadow: rgba(0, 0, 0, 0.18);
  }
  * { box-sizing: border-box; margin: 0; padding: 0; }
  html, body {
    width: 1200px;
    height: 1023px;
    overflow: hidden;
    background: var(--canvas);
    font-family: "Open Sans", Arial, sans-serif;
    color: var(--ink);
  }
  .canvas {
    position: relative;
    width: 1200px;
    height: 1023px;
  }
  .card {
    position: absolute;
    width: 600px;
    height: 343px;
    background: var(--card);
    box-shadow: 0 10px 28px var(--shadow);
    overflow: hidden;
  }
  .card--front { left: 70px; top: 90px; }
  .card--back { left: 530px; top: 560px; }

  .card__decor {
    position: absolute;
    inset: 0;
  }
  .card--front .card__decor {
    background:
      linear-gradient(120deg, rgba(60,60,60,0.55) 0%, rgba(160,160,160,0.35) 22%, rgba(255,255,255,0) 45%);
  }
  .card--back .card__decor {
    background:
      linear-gradient(160deg, var(--grey-dark) 0%, #6d6d6d 18%, var(--grey-light) 42%, rgba(251,251,251,0) 62%);
  }

  .brand {
    position: absolute;
    display: flex;
    align-items: center;
    gap: 12px;
  }
  .card--front .brand { left: 250px; top: 64px; }
  .card--back .brand { left: 190px; top: 210px; }
  .brand__square {
    width: 46px;
    height: 46px;
    background: var(--grey-dark);
  }
  .brand__text {
    font-weight: 300;
    color: var(--ink);
    line-height: 1.15;
  }
  .brand__name {
    display: block;
    font-size: 25px;
    letter-spacing: 2px;
    text-transform: uppercase;
  }
  .brand__sub {
    display: block;
    font-size: 13px;
    letter-spacing: 7px;
  }

  .contact {
    position: absolute;
    left: 40px;
    bottom: 34px;
  }
  .contact__name {
    font-size: 19px;
    font-weight: 700;
  }
  .contact__title {
    font-size: 14px;
    color: var(--ink-soft);
    margin-bottom: 18px;
  }
  .contact__line {
    font-size: 14px;
    color: var(--ink-soft);
    line-height: 1.7;
  }
  .contact__sep { padding: 0 7px; color: var(--grey-mid); }
</style>
</head>
<body>
<main class="canvas">

  <section class="card card--front" aria-label="Business card front">
    <div class="card__decor" role="img" aria-label="Soft grey gradient backdrop"></div>
    <div class="brand">
      <span class="brand__square"></span>
      <span class="brand__text">
        <span class="brand__name">Doran M. Vaske</span>
        <span class="brand__sub">Law office</span>
      </span>
    </div>
    <div class="contact">
      <p class="contact__name">Doran M. Vaske</p>
      <p class="contact__title">Attorney</p>
      <p class="contact__line">626-503-7719<span class="contact__sep">|</span>626-581-9046<span class="contact__sep">|</span>dvaske@dmvlegalgrp.example</p>
      <p class="contact__line">482 W. Harlow Ave., Suite 312, Pasadena, CA 91108</p>
    </div>
  </section>

  <section class="card card--back" aria-label="Business card back">
    <div class="card__decor" role="img" aria-label="Dark-to-light grey gradient band"></div>
    <div class="brand">
      <span class="brand__square"></span>
      <span class="brand__text">
        <span class="brand__name">Doran M. Vaske</span>
        <span class="brand__sub">Law office</span>
      </span>
    </div>
  </section>

</main>
</body>
</html>
```